Business card and company stationary - Bravora Cleaning Ltd

1. Who are we and who are our customers?

o We are a relatively new cleaning company, established December 2008. We are a small company. We have 24 staff and we offer domestic and commercial cleaning services.
o We both (me and my wife) have been working for many years in the cleaning industry. We worked for some of the biggest and best cleaning companies in UK. We’ve been operatives, supervisors and managers.
o Inevitably after so many years of working for someone else, we decided to start our own business.
o Our domestic customers are middle class families and busy professionals. We’ve got some commercial customers, mainly offices.
o We are growing steadily.

2. What do we do? What are our services?

o Cleaning. We’ve got range of services - not to many but still can be daunting and confusing for some.
o Generally we’ve got domestic and commercial clients. The approach to the domestic cleaning customers is different to the commercial. In the way we want to say that it is cleaning that we do, but we acknowledge the environment and we appreciate the personal circumstances and requirements that are present. We do care, we listen and we try to work out the best possible way to complete our work.
o Mainly we get our work through referrals

3. What do we want with our stationery ?

o To place and maintain our message and reach out to people and organisations
o We want to advertise, communicate and sale.
o We are going to sell services.
o Increase membership, loyalty and support.

We are after business card design, headed letter and compliment slip.
We would like the headed letter to be created in formats suitable for :
- printing format
- also for use in our daily correspondence via e mail with clients and staff in a easy to edit and write format

The website we have is still under contraction and the domain is bravoracleaning.example

Target Market(s)

Families, individuals, businesses.

Industry/Entity Type

Cleaning Service

Contact Information for Business Card

FRONT :
Company Name - Bravora Cleaning Ltd
Company address - 41 Pelgate Rd, Hornchurch, Essex, RM14 7QD
Name - Mrs. Radoslava Petkova - Sola
Title - Managing Director
Company phone - 020 8937 2158
E mail - sola.petkova@bravoracleaning.example

BACK :

Company website - bravoracleaning.example
E mail - enquiries@bravoracleaning.example

Font styles to use
Serif

Requirements
Must have
• The above items and company logo...maybe at the back. But I'm free for any suggestions.

```html
<!DOCTYPE html>
<html lang="en">
<head>
<meta charset="utf-8">
<title>Bravora Cleaning Ltd – Business Card</title>
<link rel="stylesheet" href="https://fonts.googleapis.com/css2?family=Mulish:wght@700&family=Questrial&display=swap">
<style>
  :root {
    --page: #ffffff;
    --card: #ffffff;
    --brand-blue: #35c6f2;
    --text-blue: #3cc3ef;
    --ink-grey: #6b6b6b;
    --pattern-tint: #eaf6fc;
    --shadow: rgba(0, 0, 0, 0.55);
  }
  html, body {
    margin: 0;
    padding: 0;
    width: 1041px;
    height: 1200px;
    overflow: hidden;
    background: var(--page);
  }
  .canvas {
    position: relative;
    width: 1041px;
    height: 1200px;
    font-family: "Questrial", "Century Gothic", sans-serif;
  }
  .card {
    position: absolute;
    background: var(--card);
    box-shadow: 14px 16px 18px var(--shadow);
    overflow: hidden;
  }
  .card--front {
    left: 173px;
    top: 160px;
    width: 686px;
    height: 384px;
  }
  .card--back {
    left: 170px;
    top: 651px;
    width: 685px;
    height: 386px;
  }
  .brand-dot {
    position: absolute;
    left: 243px;
    top: 34px;
    width: 190px;
    height: 190px;
    border-radius: 50%;
    background: var(--brand-blue);
  }
  .brand-name {
    position: absolute;
    left: 0;
    right: 0;
    top: 262px;
    text-align: center;
    color: var(--ink-grey);
    font-weight: 400;
    line-height: 1;
  }
  .brand-name__main {
    display: block;
    font-size: 62px;
    letter-spacing: 4px;
  }
  .brand-name__sub {
    display: block;
    margin-top: 10px;
    font-size: 20px;
    letter-spacing: 11px;
  }
  .pattern-field {
    position: absolute;
    inset: 0;
    background: var(--pattern-tint);
  }
  .contact {
    position: absolute;
    inset: 0;
    text-align: center;
    color: var(--text-blue);
    font-size: 22px;
  }
  .contact__line {
    position: absolute;
    left: 0;
    right: 0;
    line-height: 1;
    white-space: nowrap;
  }
  .contact__name {
    top: 42px;
    font-family: "Mulish", "Century Gothic", sans-serif;
    font-weight: 700;
    font-size: 32px;
    color: var(--ink-grey);
  }
  .contact__role    { top: 83px; }
  .contact__mobile  { top: 160px; }
  .contact__office  { top: 184px; }
  .contact__email   { top: 236px; }
  .contact__web     { top: 261px; }
  .contact__address { top: 317px; }
</style>
</head>
<body>
<main class="canvas">
  <section class="card card--front" aria-label="Business card front">
    <div class="brand-dot"></div>
    <div class="brand-name">
      <span class="brand-name__main">BRAVORA</span>
      <span class="brand-name__sub">CLEANING LTD</span>
    </div>
  </section>

  <section class="card card--back" aria-label="Business card back">
    <div class="pattern-field" role="img" aria-label="Faint repeating pattern of water drops and leaves in pale blue"></div>
    <div class="contact">
      <div class="contact__line contact__name">Mrs. Radoslava Petkova - Sola</div>
      <div class="contact__line contact__role">Managing Director</div>
      <div class="contact__line contact__mobile">Mobile: 07700 900418</div>
      <div class="contact__line contact__office">Office: 020 8937 2158</div>
      <div class="contact__line contact__email">Email: sola.petkova@bravoracleaning.example</div>
      <div class="contact__line contact__web">Web: bravoracleaning.example</div>
      <div class="contact__line contact__address">Address: 41 Pelgate Rd, Hornchurch, Essex, RM14 7QD</div>
    </div>
  </section>
</main>
</body>
</html>
```